Business Card Design and Stationary design for consulting firm

Harbourline Sourcing are looking for a new business card design and a design for their A4 letterhead / A4 invoices.

We are seeking to heavily increase our brand awareness and require a business card that's professional in appearance but also shows flare and innovation. A card design that people will remember.

About Us
Harbourline Sourcing are `The Sourcing Crew’.
Our mission is to be one of Australia’s greatest companies. Our aim is to help our customers achieve the best result from their purchasing experience.

Our Requirement:
• IMPACT! IMPACT! IMPACT!
• BUSINESS & PROFESSIONAL LOOKING

• Our business colours are orange, blue and green (See the logo attached).

We have provided an Art Design specification (attached) that needs to be followed for you to win the design. This also has the font, which is used on the logo.

We are after a two sided business card

Side One should have the:
The company Logo
The Sourcing Crew
www.harbourlinesourcing.com.au
Procure | Personnel | Probity & Privacy
Sydney | Melbourne | Adelaide | Brisbane

Side Two
Logo (optional)
Harbourline Sourcing (optional)
Employee details (details listed below)

The above format is our preferred option, but if you think you can come up with something better, feel free to put it forward.

We are leaving the design up to you, but it must incorporate the logo.

We will need a template that we can change the employee details on, as we will be adding more staff over the coming months.

The details below are for one employee per card with the same design.
------------------------

Employee Details:

Marcus Oldfield MBA, MMgmtStratProc
Principal Consultant
0412 356 917
Marcus@harbourlinesourcing.com.au

Brianna Tolhurst
Consulting Manager
0431 629 084
Brianna@harbourlinesourcing.com.au

Our website is www.harbourlinesourcing.com.au

The Letterhead / invoice needs to incorporate:
the company Logo
The Sourcing Crew
Sydney | Melbourne | Adelaide | Brisbane but otherwise the design is over to you.

This file needs to be delivered in word format as other detail will be added to the documents.

We look forward to you award winning designs. If you require any further information please feel free to contact us.

Regards
Harbourline Sourcing

Target Market(s)

Our Target market is companies with 80+ employees. The market we segment is heavily male based, between the ages of 35-55 years of age.

Industry/Entity Type

Consulting

Contact Information for Business Card

See Project Description

Font styles to use
Other font styles liked:
• See Art Specification

Requirements
Must have
• Company Colours, See Project Description
Should not have
• Be outside the Art specification guidelines

```html
<!DOCTYPE html>
<html lang="en">
<head>
<meta charset="utf-8">
<title>Harbourline Sourcing Invoice</title>
<link href="https://fonts.googleapis.com/css2?family=Open+Sans:wght@400;600;700&display=swap" rel="stylesheet">
<style>
  :root {
    --blue: #1a7dc4;
    --blue-pale: #e1eef9;
    --row-line: #e3eef8;
    --ink: #4a4a4a;
    --ink-soft: #5a5a5a;
    --green: #5aa83c;
    --orange: #f08a2c;
    --paper: #ffffff;
    --rule: #6a6a6a;
  }
  html, body { margin: 0; padding: 0; overflow: hidden; }
  body { width: 852px; height: 1200px; background: var(--paper); font-family: "Open Sans", Arial, sans-serif; color: var(--ink); }
  .invoice { position: relative; width: 852px; height: 1200px; overflow: hidden; }
  .abs { position: absolute; margin: 0; }

  .brand { left: 57px; top: 108px; display: flex; align-items: center; gap: 10px; }
  .brand-dot { width: 16px; height: 16px; border-radius: 50%; background: var(--blue); }
  .brand-name { font-size: 21px; font-weight: 600; color: var(--ink); letter-spacing: 0.5px; }

  .company-ids { right: 62px; top: 118px; text-align: right; font-size: 16px; line-height: 25px; color: var(--ink-soft); }

  .field-label { font-size: 14px; font-weight: 700; color: var(--blue); }
  .invoice-no { left: 61px; top: 196px; }
  .invoice-date { left: 611px; top: 196px; }
  .customer-line { left: 61px; font-size: 15px; color: var(--ink-soft); }

  .line-items { left: 61px; top: 328px; width: 735px; height: 536px; }
  .items-head { position: absolute; left: 0; top: 0; width: 735px; height: 37px; background: var(--blue); color: #fff; font-weight: 700; font-size: 15px; }
  .items-head span { position: absolute; top: 8px; }
  .items-body { position: absolute; left: 0; top: 37px; width: 731px; height: 497px; border: 2px solid var(--blue); border-top: none; }
  .col-divider { position: absolute; left: 589px; top: 0; width: 2px; height: 497px; background: var(--blue); }
  .row-line { position: absolute; left: 0; width: 731px; height: 3px; background: var(--row-line); }
  .items-total { position: absolute; left: 0; top: 457px; width: 731px; height: 40px; box-sizing: border-box; background: var(--blue-pale); border-top: 2px solid #cfe2f3; }
  .items-total span { position: absolute; left: 25px; top: 8px; font-weight: 700; font-size: 15px; color: var(--ink); }

  .payment { left: 61px; top: 882px; font-size: 16px; color: var(--ink-soft); }
  .bank { left: 61px; top: 928px; font-size: 16px; line-height: 22.5px; color: var(--ink-soft); }
  .bank strong { color: var(--ink); font-weight: 700; }

  .contact { left: 54px; font-size: 15.5px; color: var(--ink-soft); display: flex; align-items: center; gap: 7px; }
  .contact svg { width: 19px; height: 19px; }
  .footer-rule { left: 184px; top: 1101px; width: 616px; height: 2px; background: var(--rule); }
  .tagline-head { right: 52px; top: 1107px; font-size: 16px; font-weight: 700; color: var(--blue); }
  .tagline { right: 52px; top: 1132px; font-size: 15.5px; color: var(--ink-soft); }
  .tagline i { font-style: normal; color: var(--blue); }
</style>
</head>
<body>
<main class="invoice">
  <div class="abs brand"><span class="brand-dot"></span><span class="brand-name">Harbourline Sourcing</span></div>

  <p class="abs company-ids">ABN: 48213907651<br>ACN: 213 907 651</p>

  <p class="abs field-label invoice-no">INVOICE # :</p>
  <p class="abs field-label invoice-date">DATE :</p>
  <p class="abs customer-line" style="top:231px">Customer:</p>
  <p class="abs customer-line" style="top:259px">Address :</p>
  <p class="abs customer-line" style="top:291px">Phone :</p>

  <section class="abs line-items">
    <div class="items-head"><span style="left:29px">DESCRIPTION</span><span style="left:626px">AMOUNT</span></div>
    <div class="items-body">
      <div class="row-line" style="top:45px"></div>
      <div class="row-line" style="top:92px"></div>
      <div class="row-line" style="top:143px"></div>
      <div class="row-line" style="top:190px"></div>
      <div class="row-line" style="top:233px"></div>
      <div class="row-line" style="top:278px"></div>
      <div class="row-line" style="top:323px"></div>
      <div class="row-line" style="top:368px"></div>
      <div class="row-line" style="top:418px"></div>
      <div class="items-total"><span>Total</span></div>
      <div class="col-divider"></div>
    </div>
  </section>

  <p class="abs payment">Make all payments by direct deposit to Harbourline Sourcing Pty Limited</p>
  <p class="abs bank"><strong>The company bank account details are:</strong><br>
    Banking Institution: Tidewater Bank<br>
    Account Name: Harbourline Sourcing Pty Limited<br>
    BSB: 064218<br>
    Account Number: 518274063</p>

  <div class="abs footer-rule"></div>
  <p class="abs contact" style="top:1087px">
    <svg viewBox="0 0 20 20"><circle cx="10" cy="10" r="10" fill="var(--green)"/><path d="M6.5 5.5l2 -.5 1 2.5-1.2 1a6 6 0 0 0 3.2 3.2l1-1.2 2.5 1-.5 2c-4.5.3-8.3-3.5-8-8z" fill="#fff"/></svg>
    1300 582 416</p>
  <p class="abs contact" style="top:1111px">
    <svg viewBox="0 0 20 20"><circle cx="10" cy="10" r="10" fill="var(--blue)"/><rect x="5" y="6.5" width="10" height="7" fill="none" stroke="#fff" stroke-width="1.4"/><path d="M5 6.5l5 4 5-4" fill="none" stroke="#fff" stroke-width="1.4"/></svg>
    info@harbourlinesourcing.com.au</p>
  <p class="abs contact" style="top:1135px">
    <svg viewBox="0 0 20 20"><circle cx="10" cy="10" r="10" fill="var(--orange)"/><path d="M8.5 11.5l3-3M9 7.5l1-1a2 2 0 0 1 3 3l-1 1M11 12.5l-1 1a2 2 0 0 1-3-3l1-1" fill="none" stroke="#fff" stroke-width="1.5" stroke-linecap="round"/></svg>
    harbourlinesourcing.com.au</p>

  <p class="abs tagline-head">The Sourcing Crew</p>
  <p class="abs tagline">Source <i>|</i> Supply <i>|</i> Strategy <i>|</i> Staffing</p>
</main>
</body>
</html>
```